We are an integrated facilities management company.

We aggregate everything related to facilities maintenance. Repair-replacement of equipment and facility space materials from:
Asset gathering and tracking.
Vendor screening, contracting and management.
Service requirement development.
Work order processing and management.
Invoice reconciliation.
Vendor payment.
Reporting.
Capital equipment bids and project management.

Target Market(s)

Retail, hospitality, multi-family housing, long term healthcare.

Industry/Entity Type

Maintenance

Contact Information for Business Card

Professional and bold look. (see logo zip file)

Colors
3377b5
85abd2
cedeed

Requirements
Must have
• N/A
Nice to have
• N/A
Should not have
• N/A

```html
<!DOCTYPE html>
<html lang="en">
<head>
<meta charset="utf-8">
<title>Brightwell Services – Business Card</title>
<link rel="stylesheet" href="https://fonts.googleapis.com/css2?family=Open+Sans:wght@400;700&display=swap">
<style>
  :root {
    --backdrop: #545454;
    --brand-blue: #0755a0;
    --brand-blue-deep: #064a8e;
    --ink-blue: #0b4f9e;
    --ink-grey: #555a60;
    --paper: #ffffff;
  }
  * { margin: 0; padding: 0; box-sizing: border-box; }
  html, body {
    width: 1200px; height: 897px; overflow: hidden;
    background: var(--backdrop);
    font-family: "Open Sans", Arial, sans-serif;
  }
  .canvas { position: relative; width: 1200px; height: 897px; }
  .card {
    position: absolute; top: 148px;
    width: 335px; height: 584px;
  }
  .card--back { left: 213px; background: var(--brand-blue); }
  .card--front { left: 646px; background: var(--paper); }

  .back-name {
    position: absolute; left: 0; right: 0; top: 270px;
    text-align: center;
    font-weight: 700; font-size: 30px; letter-spacing: 1px;
    color: var(--brand-blue-deep);
  }

  .brand-name {
    position: absolute; left: 38px; top: 286px; top: 138px;
    font-weight: 700; font-size: 20px; letter-spacing: 0.5px;
    color: var(--ink-blue);
    white-space: nowrap;
  }

  .holder { position: absolute; left: 38px; top: 328px; }
  .holder-name {
    font-weight: 700; font-size: 22px; letter-spacing: 0.3px;
    color: var(--ink-blue); line-height: 1.2;
  }
  .holder-role { font-size: 16px; color: var(--ink-grey); margin-top: 2px; }

  .address {
    position: absolute; left: 38px; top: 397px;
    font-size: 16px; line-height: 22px; color: var(--ink-grey);
  }

  .contacts {
    position: absolute; left: 38px; top: 467px;
    list-style: none;
    font-size: 16px; line-height: 22px; color: var(--ink-grey);
  }
  .contacts li { display: flex; align-items: center; gap: 6px; }
  .contacts svg { width: 13px; height: 13px; fill: var(--ink-blue); flex: none; }
</style>
</head>
<body>
<div class="canvas">
  <section class="card card--back" aria-label="Card back">
    <div class="back-name">BRIGHTWELL</div>
  </section>

  <section class="card card--front" aria-label="Card front">
    <div class="brand-name">BRIGHTWELL SERVICES</div>

    <div class="holder">
      <div class="holder-name">DANIEL REYES</div>
      <div class="holder-role">President</div>
    </div>

    <address class="address" style="font-style:normal">
      1180 Harbor View Lane<br>
      Seacliff CA 90410
    </address>

    <ul class="contacts">
      <li>
        <svg viewBox="0 0 24 24" aria-hidden="true"><path d="M6.6 10.8a15.1 15.1 0 0 0 6.6 6.6l2.2-2.2a1 1 0 0 1 1-.25 11.4 11.4 0 0 0 3.6.57 1 1 0 0 1 1 1V20a1 1 0 0 1-1 1A17 17 0 0 1 3 4a1 1 0 0 1 1-1h3.5a1 1 0 0 1 1 1c0 1.25.2 2.45.57 3.57a1 1 0 0 1-.25 1z"/></svg>
        555-014-2290
      </li>
      <li>
        <svg viewBox="0 0 24 24" aria-hidden="true"><path d="M2 5h20v2l-10 6L2 7z"/><path d="M2 9l10 6 10-6v10H2z"/></svg>
        info@brightwellfs.com
      </li>
      <li>
        <svg viewBox="0 0 24 24" aria-hidden="true"><path d="M12 2a10 10 0 1 0 0 20 10 10 0 0 0 0-20zm-1 17.9A8 8 0 0 1 4.1 10L9 15v1a2 2 0 0 0 2 2zm6.9-2.5A2 2 0 0 0 16 16h-1v-3a1 1 0 0 0-1-1H8v-2h2a1 1 0 0 0 1-1V7h2a2 2 0 0 0 2-2v-.4a8 8 0 0 1 2.9 12.8z"/></svg>
        www.brightwellfs.com
      </li>
    </ul>
  </section>
</div>
</body>
</html>
```